Limber Nest

brand name is varlo
300g package
collagen product containing bovine collagen peptides
orange packaging color
with turmeric added
ultimate complex for joints flexibility & mobility
ingredients
collagen, turmeric curcumin, vitamin c
a product that takes care of the joints mobility and provides resilience against injuries

similar design to the packaging in the files

Target Market(s)

fitness, health products

Industry/Entity Type

health and fitness

Colors
F0912C
F2A743
F7CA91
FBE8D2
FDF5EE

Requirements
Must have
• very clear message of the advantage of the product which is providing flexible joints, increased mobility, great inflammation response, amazing skin hair bones and nails care
Nice to have
• turmeric design or something that indicates the product containing organic turmeric, orange fresh design, something to makes me feel happy with movement of my body/joints

```html
<!DOCTYPE html>
<html lang="en">
<head>
<meta charset="utf-8">
<title>Varlo Collagen Peptides – Turmeric</title>
<link rel="stylesheet" href="https://fonts.googleapis.com/css2?family=Poppins:wght@500;600;700;800&family=Roboto+Condensed:wght@600;700&display=swap">
<style>
  :root {
    --backdrop: #ececec;
    --orange-deep: #e2861f;
    --orange: #f0912c;
    --orange-light: #f7b566;
    --white: #ffffff;
    --cream: #fdf5ee;
  }
  html, body {
    margin: 0;
    padding: 0;
    width: 1051px;
    height: 1200px;
    overflow: hidden;
    background: var(--backdrop);
  }
  .pack {
    position: absolute;
    left: 236px;
    top: 190px;
    width: 587px;
    height: 766px;
    border-radius: 26px 26px 4px 4px;
    background: linear-gradient(100deg, var(--orange-deep) 0%, var(--orange) 45%, var(--orange-light) 100%);
    color: var(--white);
    font-family: "Poppins", sans-serif;
  }
  .pack > * { position: absolute; margin: 0; }
  .brand {
    left: 0; right: 0; top: 166px;
    text-align: center;
    font-weight: 800;
    font-size: 64px;
    letter-spacing: 4px;
    line-height: 1;
  }
  .product-name {
    left: 0; right: 0; top: 262px;
    text-align: center;
    font-weight: 800;
    font-size: 70px;
    line-height: 1;
    letter-spacing: -2px;
  }
  .product-type {
    left: 0; right: 0; top: 330px;
    text-align: center;
    font-family: "Roboto Condensed", sans-serif;
    font-weight: 700;
    font-size: 31px;
    line-height: 1;
  }
  .tagline {
    left: 0; right: 0; top: 366px;
    text-align: center;
    font-weight: 600;
    font-size: 12px;
    letter-spacing: 0.4px;
    line-height: 1;
  }
  .benefits {
    left: 117px; top: 386px;
    list-style: none;
    padding: 0;
    font-weight: 500;
    font-size: 15px;
  }
  .benefits li {
    display: flex;
    align-items: center;
    height: 25px;
  }
  .benefits svg { margin-right: 6px; flex: none; }
  .flavour {
    left: 121px; top: 491px;
    width: 184px; height: 41px;
    background: var(--cream);
    color: var(--orange-deep);
    font-family: "Roboto Condensed", sans-serif;
    font-weight: 700;
    font-size: 27px;
    line-height: 41px;
    text-align: center;
  }
  .turmeric-art {
    left: 321px; top: 441px;
    width: 154px; height: 157px;
    border-radius: 40% 50% 45% 55%;
    background: radial-gradient(circle at 40% 40%, rgba(253,245,238,0.3), rgba(251,232,210,0.06));
  }
  .ingredients-title {
    left: 121px; top: 550px;
    font-weight: 600;
    font-size: 13px;
    padding-bottom: 2px;
    border-bottom: 1px solid var(--white);
  }
  .ingredients-list {
    left: 122px; top: 576px;
    font-weight: 600;
    font-size: 12px;
  }
  .supplement {
    left: 123px; top: 626px;
    font-weight: 700;
    font-size: 21px;
    line-height: 21px;
  }
  .net-weight {
    left: 125px; top: 675px;
    font-weight: 600;
    font-size: 16.5px;
  }
  .seal {
    left: 371px; top: 607px;
  }
</style>
</head>
<body>
  <main class="pack">
    <p class="brand">VARLO</p>
    <h1 class="product-name">COLLAGEN</h1>
    <p class="product-type">PEPTIDES TYPE I &amp; III</p>
    <p class="tagline">ultimate complex for joints flexibility &amp; mobility</p>

    <ul class="benefits">
      <li>
        <svg width="20" height="20" viewBox="0 0 22 22"><circle cx="11" cy="11" r="10" fill="none" stroke="#fff" stroke-width="1.2"/><circle cx="11" cy="11" r="4" fill="none" stroke="#fff" stroke-width="1.2"/></svg>
        skin, hair, bones and nails care
      </li>
      <li>
        <svg width="20" height="20" viewBox="0 0 22 22"><circle cx="11" cy="11" r="10" fill="none" stroke="#fff" stroke-width="1.2"/><path d="M6 11h10M12 7l4 4-4 4" fill="none" stroke="#fff" stroke-width="1.4"/></svg>
        increased mobility
      </li>
      <li>
        <svg width="20" height="20" viewBox="0 0 22 22"><circle cx="11" cy="11" r="10" fill="none" stroke="#fff" stroke-width="1.2"/><path d="M6 11.5l3.5 3.5L16 8" fill="none" stroke="#fff" stroke-width="1.4"/></svg>
        providing flexible joints
      </li>
      <li>
        <svg width="20" height="20" viewBox="0 0 22 22"><circle cx="11" cy="11" r="10" fill="none" stroke="#fff" stroke-width="1.2"/><path d="M11 5.5v11M5.5 11h11" fill="none" stroke="#fff" stroke-width="1.4"/></svg>
        great inflammation response
      </li>
    </ul>

    <p class="flavour">TURMERIC</p>
    <div class="turmeric-art" role="img" aria-label="Line drawing of turmeric root"></div>

    <p class="ingredients-title">INGREDIENTS</p>
    <p class="ingredients-list">COLLAGEN, TURMERIC CURCUMIN, VITAMIN C</p>

    <p class="supplement">DIETARY<br>SUPPLEMENT</p>
    <p class="net-weight">NET WT 11OZ (300 G)</p>

    <svg class="seal" width="72" height="72" viewBox="0 0 74 74" role="img" aria-label="Quality seal">
      <circle cx="37" cy="37" r="36" fill="#fff"/>
      <circle cx="37" cy="37" r="32" fill="none" stroke="#f0912c" stroke-width="1.5"/>
      <rect x="5" y="35" width="64" height="4" fill="#f0912c"/>
    </svg>
  </main>
</body>
</html>
```